New audiology website PSD design only - guaranteed

We need a clean and attractive website to replace an existing Audiology (hearing technology) website which will be wordpress based.
The current website is: http://pelmorahearing.com.au
They have a new logo and colors which you can find at www.quodel.net/temp/plh2018.pdf
We will no longer have a web shop in the new website
To enter the competition, we only need a sample of the home page.
The winning design will be asked to produce 2 standard page template alternatives as well (based on the winning home page design, but for a standard page layout)
The winning design must provide any photos used
We want a clean, credible site but with some warmth
Target Market(s)
All ages but needs to include the elderly
Industry/Entity Type
Medical And Science
Number of Pages Required
3 page
Look and feel
Each slider illustrates characteristics of the customer's brand and the style your logo design should communicate.

```html
<!DOCTYPE html>
<html lang="en">
<head>
<meta charset="utf-8">
<title>Pelmora Hearing</title>
<link rel="stylesheet" href="https://fonts.googleapis.com/css2?family=Open+Sans:wght@400;600;700&family=Tinos:wght@400;700&display=swap">
<style>
:root{
  --orange:#f26a21;
  --orange-dark:#d9571a;
  --ink:#2b2b2b;
  --text:#555;
  --muted:#8a8a8a;
  --light:#f4f4f4;
  --line:#e3e3e3;
  --white:#fff;
  --footer:#333333;
  --nav-gray:#4a4a4a;
  --serif:'Tinos', 'Times New Roman', serif;
  --sans:'Open Sans', Arial, sans-serif;
}
*{box-sizing:border-box;margin:0;padding:0}
html,body{width:1200px;height:3896px;overflow:hidden}
body{position:relative;background:var(--white);font-family:var(--sans);color:var(--text)}
.abs{position:absolute}
a{color:inherit;text-decoration:none}
h1,h2,h3,h4,h5,h6{font-weight:400}

/* nav */
.topbar{top:0;left:0;width:1200px;height:65px}
.topbar .menu{left:109px;top:0;width:779px;height:65px;background:var(--orange);display:flex;align-items:center}
.topbar .menu a{color:#fff;font-size:13px;font-weight:600;padding:0 14px;height:65px;line-height:65px}
.topbar .menu a.active{background:var(--nav-gray)}
.topbar .account{left:888px;top:0;width:203px;height:65px;background:var(--nav-gray);display:flex;align-items:center;justify-content:center;gap:14px}
.btn-sm{font-size:13px;font-weight:600;color:#fff;padding:5px 14px;border-radius:2px;background:var(--orange)}
.btn-sm.ghost{background:transparent;border:1px solid #fff}

.brand{top:100px;left:0;width:1200px;text-align:center;display:flex;justify-content:center;align-items:center;gap:10px}
.brand .dot{width:34px;height:34px;border-radius:50%;background:var(--orange)}
.brand .name{font-family:var(--sans);font-weight:700;font-size:36px;color:#555}

/* hero */
.hero{top:200px;left:0;width:1200px;height:488px;background:linear-gradient(110deg,#5f6b4e 0%,#8a8a6a 35%,#c7b9a2 60%,#9b8e80 100%)}
.hero-text{left:240px;top:372px;width:260px;text-align:center;color:#fff}
.hero-text h1{font-family:var(--serif);font-size:28px;font-weight:400}
.hero-text p{font-size:12px;line-height:17px;margin:10px 0 12px}
.btn{display:inline-block;background:var(--orange);color:#fff;font-size:12px;padding:6px 22px;border-radius:14px}
.hero-arrow{top:433px;width:20px;height:20px;border-radius:50%;display:flex;align-items:center;justify-content:center}

/* section titles */
.title{left:0;width:1200px;text-align:center;font-family:var(--serif);font-size:26px;color:var(--ink)}
.title b{font-weight:700}
.title span{font-weight:400;color:#666}

/* services */
.services{top:688px;left:0;width:1200px;height:429px;background:var(--light)}
.card{width:255px;height:228px;background:#fff;box-shadow:0 3px 8px rgba(0,0,0,.12);text-align:center;padding:22px 26px 0}
.card h3{font-family:var(--serif);font-size:17px;font-weight:700;color:var(--ink);margin:8px 0 10px}
.card p{font-size:12px;line-height:16px}
.card .more{display:block;margin-top:6px;color:var(--orange);font-size:12px}
.card.featured{background:var(--orange);color:#fff}
.card.featured h3,.card.featured .more{color:#fff}

/* products */
.product{top:1241px;width:221px;height:198px;background:linear-gradient(160deg,#d6d8de,#a7abb6)}
.product.p1{background:linear-gradient(160deg,#f4a56b,#e9763a);border:3px solid var(--orange)}
.product.p3{background:linear-gradient(160deg,#c9cbd3,#8d7aa7)}
.product.p4{background:linear-gradient(160deg,#e6e6ea,#b64a3c)}
.caption{top:1478px;width:221px;text-align:center;font-size:12px;line-height:16px;color:#444}
.arrow-dot{width:18px;height:18px;border-radius:50%;display:flex;align-items:center;justify-content:center}

/* doctors */
.doctors-band{top:1662px;left:0;width:1200px;height:332px;background:var(--light)}
.doctors-text{left:122px;top:1720px;width:450px}
.doctors-text h2{font-family:var(--serif);font-size:25px;color:var(--ink);font-weight:700;margin-bottom:18px}
.doctors-text h2 span{font-weight:400;color:#666}
.doctors-text p{font-size:12.5px;line-height:17px;margin-bottom:20px}
.doctor-photo{left:623px;top:1652px;width:447px;height:353px;background:linear-gradient(120deg,#dde3e8,#b9c4cc 50%,#8a97a3)}

/* reviews */
.review{top:2168px;width:300px;height:260px;text-align:center;padding:40px 30px 0}
.review h4{font-family:var(--serif);font-size:16px;font-weight:700;color:var(--ink);margin-top:10px}
.review .role{font-family:var(--serif);font-size:12px;margin-bottom:12px}
.review p{font-size:12.5px;line-height:17px}
.review.featured{background:var(--orange);color:#fff}
.review.featured h4{color:#fff}
.dots{display:flex;gap:6px;justify-content:center}
.dots i{width:8px;height:8px;border-radius:50%;background:#bbb}
.dots i.on{background:var(--orange)}

/* appointment + blog */
.appointment-band{top:2576px;left:0;width:1200px;height:587px;background:var(--light)}
.form{left:148px;top:2644px;width:374px}
.form h2{font-family:var(--serif);font-size:25px;color:var(--ink);text-align:center;margin-bottom:20px;font-weight:700}
.form h2 span{font-weight:400;color:#666}
.field{height:36px;background:#fff;border:1px solid var(--line);margin-bottom:17px;font-family:var(--serif);font-size:12px;color:#888;padding:0 14px;line-height:34px;position:relative}
.send{height:26px;background:var(--orange);border-radius:14px;color:#fff;text-align:center;font-size:12px;line-height:26px;margin-top:2px}
.blog{left:600px;top:2623px;width:478px;height:475px;background:#fff;box-shadow:0 2px 6px rgba(0,0,0,.06)}
.blog h2{font-family:var(--serif);font-size:25px;font-weight:700;color:var(--ink);text-align:center;margin-top:30px}
.blog .sub{font-size:12px;text-align:center;width:200px;margin:6px auto 0;line-height:16px}
.post{left:21px;top:120px;width:436px;height:200px;background:var(--light)}
.post-photo{left:10px;top:18px;width:150px;height:170px;background:linear-gradient(150deg,#b7bfc6,#5c6670)}
.post-body{left:175px;top:14px;width:250px;font-size:12px;line-height:16px}
.post-body h5{font-family:var(--serif);font-size:15px;font-weight:700;color:var(--ink);margin-bottom:10px}
.post-body .meta{display:flex;justify-content:space-between;font-size:11px;margin-bottom:8px}

/* newsletter */
.newsletter-title{top:3250px;left:0;width:1200px;text-align:center;font-family:var(--serif);font-size:28px;font-weight:400;color:var(--ink);letter-spacing:1px}
.newsletter-title b{font-weight:700}
.subscribe{left:325px;top:3306px;width:550px;height:36px;border:1px solid #ccc;border-radius:18px;overflow:hidden;display:flex}
.subscribe .input{flex:1;font-size:13px;color:#999;padding-left:16px;line-height:34px}
.subscribe .go{width:120px;background:var(--orange);color:#fff;font-weight:700;font-size:13px;text-align:center;line-height:34px}

/* footer */
.footer{top:3433px;left:0;width:1200px;height:463px;background:var(--footer);color:#ddd}
.f-brand{left:114px;top:66px;display:flex;align-items:center;gap:8px}
.f-brand .dot{width:26px;height:26px;border-radius:50%;background:var(--orange)}
.f-brand .name{font-weight:700;font-size:24px;color:#fff}
.f-about{left:114px;top:120px;width:250px;font-size:12.5px;line-height:17px}
.f-about a{color:var(--orange)}
.social{left:114px;top:222px;display:flex;gap:10px}
.social i{width:28px;height:28px;border:1.5px solid #ddd;border-radius:50%}
.f-head{font-family:var(--serif);font-size:19px;color:#fff;font-weight:700}
.links{left:416px;top:58px}
.links ul{list-style:none;margin-top:20px}
.links li{font-size:12px;line-height:24px;padding-left:12px;position:relative;color:#eee}
.links li::before{content:"";position:absolute;left:0;top:10px;width:5px;height:5px;border-radius:50%;background:var(--orange)}
.office{font-size:12px;line-height:17px;width:230px}
.office h6{font-family:var(--serif);font-size:15px;font-weight:700;color:#fff;margin-bottom:14px}
.office .row{display:flex;gap:8px;margin-bottom:6px}
.office .row svg{flex:none;margin-top:3px}
.map{width:142px;height:90px;margin-top:8px;background:linear-gradient(135deg,#e9e6dc,#cfd8c9)}
.f-rule{left:114px;top:392px;width:978px;height:1px;background:#777}
.f-copy{left:114px;top:423px;font-size:12.5px}
.f-terms{left:950px;top:423px;width:142px;text-align:right;font-size:12.5px}
</style>
</head>
<body>

<header class="abs topbar">
  <nav class="abs menu">
    <a class="active">Home</a><a>Your Hearing</a><a>Hearing Aids</a><a>Musicians</a><a>Doctors Information</a><a>About</a><a>Products</a><a>Contact</a>
  </nav>
  <div class="abs account"><span class="btn-sm ghost">Login</span><span class="btn-sm">SignUp</span></div>
</header>

<div class="abs brand"><span class="dot"></span><span class="name">Pelmora Hearing</span></div>

<section class="abs hero" role="img" aria-label="Smiling older couple seated together outdoors in a garden"></section>
<div class="abs hero-text">
  <h1>Pelmora Hearing</h1>
  <p>Pelmora Hearing is an independently owned and managed professional audiology clinic.</p>
  <span class="btn">Read More</span>
</div>
<div class="abs hero-arrow" style="left:52px;background:rgba(0,0,0,.35)"><svg width="8" height="10"><path d="M6 1 2 5l4 4" stroke="#fff" stroke-width="1.6" fill="none"/></svg></div>
<div class="abs hero-arrow" style="left:1128px;background:var(--orange)"><svg width="8" height="10"><path d="M2 1l4 4-4 4" stroke="#fff" stroke-width="1.6" fill="none"/></svg></div>

<section class="abs services">
  <h2 class="abs title" style="top:44px"><b>Our</b> <span>Services</span></h2>
  <div class="abs card" style="left:171px;top:112px">
    <svg width="46" height="40" viewBox="0 0 46 40" fill="none" stroke="#f26a21" stroke-width="2"><path d="M4 8h26a8 8 0 0 1 0 16H4z"/><path d="M30 10l12-5v22l-12-5"/><path d="M12 24l-3 14h7l3-14"/></svg>
    <h3>Adult Hearing Test</h3>
    <p>Pure Tone Audiometry is the standard behavioural procedure for measurin...</p>
    <span class="more">Read More... &#9675;</span>
  </div>
  <div class="abs card featured" style="left:470px;top:112px">
    <svg width="40" height="40" viewBox="0 0 40 40" fill="none" stroke="#fff" stroke-width="2"><path d="M12 16a9 9 0 0 1 18 0c0 7-6 8-7 14a6 6 0 0 1-10 2"/><path d="M17 16a4 4 0 0 1 8 0c0 3-3 4-3 6"/></svg>
    <h3>Hearing Aids</h3>
    <p>When considering a hearing aid it is important that you understand your hearing los...</p>
    <span class="more">Read More...</span>
  </div>
  <div class="abs card" style="left:766px;top:112px">
    <svg width="40" height="40" viewBox="0 0 40 40" fill="none" stroke="#f26a21" stroke-width="2"><path d="M7 26V20a13 13 0 0 1 26 0v6"/><rect x="5" y="24" width="7" height="11" rx="2"/><rect x="28" y="24" width="7" height="11" rx="2"/></svg>
    <h3>Musicians</h3>
    <p>Pelmora Hearing are resellers for Tonrell and Marsden Audio and we stock samples at our clinic.</p>
    <span class="more">Read More...</span>
  </div>
</section>

<h2 class="abs title" style="top:1158px"><b>Our</b> <span>Products</span></h2>
<div class="abs arrow-dot" style="left:52px;top:1330px;background:#333"><svg width="8" height="10"><path d="M6 1 2 5l4 4" stroke="#fff" stroke-width="1.6" fill="none"/></svg></div>
<div class="abs arrow-dot" style="left:1128px;top:1330px;background:var(--orange)"><svg width="8" height="10"><path d="M2 1l4 4-4 4" stroke="#fff" stroke-width="1.6" fill="none"/></svg></div>
<div class="abs product p1" style="left:135px" role="img" aria-label="Tub and box of hearing aid drying capsules"></div>
<div class="abs product" style="left:371px" role="img" aria-label="Colourful custom moulded hearing protection earpieces"></div>
<div class="abs product p3" style="left:610px" role="img" aria-label="Boxed earbands for swimming"></div>
<div class="abs product p4" style="left:847px" role="img" aria-label="Packs of zinc hearing aid batteries"></div>
<p class="abs caption" style="left:135px">Corvane Dri-Pak drying<br>Capsules</p>
<p class="abs caption" style="left:371px">Custom Moulded Solid<br>Hearsavers</p>
<p class="abs caption" style="left:610px">Earbands for<br>Swimming</p>
<p class="abs caption" style="left:847px">Voltara Zinc<br>Batteries</p>
<div class="abs" style="left:0;top:1553px;width:1200px;text-align:center"><span class="btn">View More</span></div>

<section class="abs doctors-band"></section>
<div class="abs doctors-text">
  <h2>Doctors <span>Information</span></h2>
  <p>Pelmora Hearing is one of Sydney's leading diagnostic hearing and balance clinics.Referring doctors can be assured that all testing and rehabilitation is reviewed to the highest industry standards.Our Audiologists also work closely with referring ENT's and Doctors to ensure all testing meets the needs of their practice.</p>
  <span class="btn">Read More</span>
</div>
<div class="abs doctor-photo" role="img" aria-label="Doctor in white coat talking with a patient"></div>

<h2 class="abs title" style="top:2087px"><b>Customers</b> <span>Reviews</span></h2>
<div class="abs review" style="left:148px">
  <svg width="40" height="32" viewBox="0 0 40 32" fill="#333"><path d="M0 32V16Q0 4 12 0l2 4Q7 8 7 14h9v18zM22 32V16q0-12 12-16l2 4q-7 4-7 10h9v18z"/></svg>
  <h4>MARTIN HALE</h4><div class="role">Creative Director</div>
  <p>Lorem Ipsum is simply dummy text of the printing and typesetting industry. Lorem Ipsum has been the industry's standard dummy</p>
</div>
<div class="abs review featured" style="left:448px">
  <svg width="40" height="32" viewBox="0 0 40 32" fill="#fff"><path d="M0 32V16Q0 4 12 0l2 4Q7 8 7 14h9v18zM22 32V16q0-12 12-16l2 4q-7 4-7 10h9v18z"/></svg>
  <h4>MARTIN HALE</h4><div class="role">Creative Director</div>
  <p>Lorem Ipsum is simply dummy text of the printing and typesetting industry. Lorem Ipsum has been the industry's standard dummy</p>
</div>
<div class="abs review" style="left:806px">
  <svg width="40" height="32" viewBox="0 0 40 32" fill="#333"><path d="M0 32V16Q0 4 12 0l2 4Q7 8 7 14h9v18zM22 32V16q0-12 12-16l2 4q-7 4-7 10h9v18z"/></svg>
  <h4>MARTIN HALE</h4><div class="role">Creative Director</div>
  <p>Lorem Ipsum is simply dummy text of the printing and typesetting industry. Lorem Ipsum has been the industry's standard dummy</p>
</div>
<div class="abs dots" style="left:0;top:2450px;width:1200px"><i class="on"></i><i></i><i></i></div>
<div class="abs" style="left:0;top:2500px;width:1200px;text-align:center"><span class="btn">View More</span></div>

<section class="abs appointment-band"></section>
<div class="abs form">
  <h2>Make An <span>Appointment</span></h2>
  <div class="field">Name</div>
  <div class="field">E-Mail</div>
  <div class="field">Phone</div>
  <div class="field">Address</div>
  <div class="field">Date<svg style="position:absolute;right:14px;top:14px" width="10" height="6"><path d="M0 0h10L5 6z" fill="#999"/></svg></div>
  <div class="field">Time</div>
  <div class="send">Send</div>
</div>
<div class="abs blog">
  <h2>Latest Blogs</h2>
  <p class="sub">Lorem Ipsum is simply dummy text of the printing.</p>
  <div class="abs" style="left:410px;top:34px;display:flex;gap:5px">
    <span class="arrow-dot" style="background:#333"><svg width="8" height="10"><path d="M6 1 2 5l4 4" stroke="#fff" stroke-width="1.6" fill="none"/></svg></span>
    <span class="arrow-dot" style="background:var(--orange)"><svg width="8" height="10"><path d="M2 1l4 4-4 4" stroke="#fff" stroke-width="1.6" fill="none"/></svg></span>
  </div>
  <div class="abs post">
    <div class="abs post-photo" role="img" aria-label="Audiologist fitting a patient with hearing equipment"></div>
    <div class="abs post-body">
      <h5>Lorem Ipsum</h5>
      <div class="meta"><span>By &nbsp;MARTIN HALE</span><span>Feb 19,2018</span></div>
      <p>Lorem Ipsum is simply dummy text of the printing and typesetting industry. Lorem Ipsum has been the industry's standard dummy text.</p>
      <p style="margin-top:8px">Read More... &#9675;</p>
    </div>
  </div>
  <div class="abs dots" style="left:0;top:362px;width:478px"><i class="on"></i><i></i><i></i></div>
  <div class="abs" style="left:0;top:396px;width:478px;text-align:center"><span class="btn">View More</span></div>
</div>

<h2 class="abs newsletter-title"><b>SUBSCRIBE</b> TO OUR NEWSLETTER</h2>
<div class="abs subscribe"><span class="input">Your E-Mail</span><span class="go">SUBMIT</span></div>

<footer class="abs footer">
  <div class="abs f-brand"><span class="dot"></span><span class="name">Pelmora Hearing</span></div>
  <p class="abs f-about">Pelmora Hearing is an independently owned and managed professional audiology clinic<br><a>Read More... &#9675;</a></p>
  <div class="abs social"><i></i><i></i><i></i></div>
  <div class="abs links">
    <div class="f-head">Quick Link</div>
    <ul><li>Home</li><li>Your Hearing</li><li>Hearing Aids</li><li>Musicians</li><li>Doctors Info</li><li>About</li><li>Products</li><li>Contact</li></ul>
  </div>
  <div class="abs f-head" style="left:597px;top:58px">Contact Us</div>
  <div class="abs office" style="left:597px;top:104px">
    <h6>Kellmont</h6>
    <div class="row"><svg width="8" height="10"><path d="M4 10C1 6 0 5 0 4a4 4 0 0 1 8 0c0 1-1 2-4 6z" fill="#ddd"/></svg><span>Ground Floor, Suite 3, 42 Harbour Road Kellmont, NSW, 2071</span></div>
    <div class="row"><svg width="8" height="10"><path d="M1 0h2l1 3-1 1q1 2 3 3l1-1 1 1v2q-5 0-8-7z" fill="#ddd"/></svg><span>(02) 9000 4121</span></div>
    <div class="row"><svg width="8" height="10"><circle cx="4" cy="5" r="3.5" stroke="#ddd" fill="none"/></svg><span>Monday to Friday 9am to 5pm</span></div>
    <div class="map" role="img" aria-label="Street map of the Kellmont clinic location"></div>
  </div>
  <div class="abs office" style="left:870px;top:104px">
    <h6>Ashvale</h6>
    <div class="row"><svg width="8" height="10"><path d="M4 10C1 6 0 5 0 4a4 4 0 0 1 8 0c0 1-1 2-4 6z" fill="#ddd"/></svg><span>Shop 9, 118 Westbury Road Ashvale, NSW, 2039</span></div>
    <div class="row"><svg width="8" height="10"><path d="M1 0h2l1 3-1 1q1 2 3 3l1-1 1 1v2q-5 0-8-7z" fill="#ddd"/></svg><span>(02) 9000 7735</span></div>
    <div class="row"><svg width="8" height="10"><circle cx="4" cy="5" r="3.5" stroke="#ddd" fill="none"/></svg><span>Monday to Friday 9am to 5pm</span></div>
    <div class="map" role="img" aria-label="Street map of the Ashvale clinic location"></div>
  </div>
  <div class="abs f-rule"></div>
  <div class="abs f-copy">CopyRight &copy; &nbsp;2018 Pelmora Hearing . &nbsp;All Right Reserve</div>
  <div class="abs f-terms">Terms &amp; Conditions</div>
</footer>

</body>
</html>
```